CSP 4 side flyer for industrial trace heating services

We are an electrical trace heating specialist wanting to expand our full EPC service to the CSP (concentrated solar power) industry. We need a flyer showing our USPs and capabilities so we can promote ourselves with the view to becoming an approved vendor to bid for work.
This flyer will be distributed to end user companys like Qasir Petrolux, Novar, TDM, Melvo etc along with contracting companies working on these sites whom would usually sub contract heat tracing work to companies like ours.
Much of our potential new business will be in the Middle East. However companies we work with are usually largest international firms.
The direct route to the supply chain first involves pre-qualification. A strong brand can help us ensure people take notice of us and help us through that process. We will also be making market visits and meeting contractors and end users on their sites so this new image will be followed through to our presentations and sub section of our website.

Target Market(s)

EPCs looking to outsource the CSP plant trace heating packages.

Industry/Entity Type

Power Generation

Colors
ec1f27

Requirements
Must have
• a sales focused edge.
• industrial feel
• high level appeal
Nice to have
• images.. we are short on the ground on royalty free CSP plant images

```html
<!DOCTYPE html>
<html lang="en">
<head>
<meta charset="utf-8">
<title>Vexa Trace Heating – CSP Flyer</title>
<link rel="stylesheet" href="https://fonts.googleapis.com/css2?family=Open+Sans:wght@400;600;700;800&display=swap">
<style>
  :root{
    --red:#ec1f27;
    --ink:#1d1d1f;
    --charcoal:#2a2a2c;
    --black:#111112;
    --grey:#8a8c90;
    --mist:#e4e5e7;
    --paper:#ffffff;
    --backdrop:#d9dadc;
    --text:#4a4b4e;
  }
  *{box-sizing:border-box;margin:0;padding:0}
  html,body{width:898px;height:1200px;overflow:hidden}
  body{background:var(--backdrop);font-family:"Open Sans",Arial,sans-serif;color:var(--text);position:relative}
  .page{position:absolute;overflow:hidden;box-shadow:0 2px 8px rgba(0,0,0,.25)}
  .cover-back{left:20px;top:18px;width:429px;height:620px;background:var(--paper)}
  .cover-front{left:449px;top:18px;width:429px;height:620px;background:linear-gradient(160deg,#3a3b3e 0%,var(--black) 70%)}
  .inner-left{left:30px;top:700px;width:419px;height:485px;background:var(--paper)}
  .inner-right{left:449px;top:700px;width:419px;height:485px;background:var(--paper)}
  .deco{position:absolute;left:0;top:0}

  .brand{position:absolute;display:flex;align-items:center;gap:8px;font-weight:800;font-size:15px;letter-spacing:.5px;color:var(--ink);text-transform:uppercase;line-height:1}
  .brand-mark{width:14px;height:14px;background:var(--red)}
  .cover-back .brand{left:112px;top:40px}

  .usp-list{position:absolute;left:34px;top:190px;width:250px;list-style:none}
  .usp-list li{font-size:8px;line-height:1.5;padding-left:11px;position:relative;margin-bottom:3px;color:var(--ink)}
  .usp-list li::before{content:"";position:absolute;left:0;top:4px;width:5px;height:5px;background:var(--red)}

  .features{position:absolute;left:34px;top:320px;width:330px}
  .features p{font-size:7.5px;line-height:1.5;margin-bottom:5px}
  .features strong{color:var(--ink);font-weight:700}

  .contact{position:absolute;left:34px;top:455px;width:300px;font-size:8px;line-height:1.6;color:var(--ink)}
  .contact .red{color:var(--red);font-weight:700}
  .web{position:absolute;left:34px;bottom:40px;font-size:11px;font-weight:700;color:var(--ink)}

  .logo-box{position:absolute;left:50px;top:22px;width:230px;height:60px;background:var(--paper);display:flex;align-items:center;justify-content:center}
  .logo-box .brand{position:static}
  .headline{position:absolute;left:34px;top:190px;width:190px;padding:16px 14px;background:var(--red);color:var(--paper);font-weight:800;font-size:17px;line-height:1.2;text-transform:uppercase}
  .photo{position:absolute}
  .front-photo{left:0;top:0;width:429px;height:620px}
  .front-copy{position:absolute;left:34px;top:480px;width:360px;color:var(--paper);font-size:9px;line-height:1.5}
  .front-web{position:absolute;left:34px;top:540px;color:var(--red);font-size:10px;font-weight:700}

  .band-photo{left:0;top:0;width:419px;height:80px;background:linear-gradient(180deg,#2b3a52 0%,#5b6f8d 60%,#a9b3c0 100%)}
  .section{position:absolute}
  .section h3{font-size:9px;font-weight:800;color:var(--ink);text-transform:uppercase;margin-bottom:4px}
  .section p{font-size:6.5px;line-height:1.55}
  .s-design{left:22px;top:92px;width:375px}
  .s-materials{left:22px;top:210px;width:375px}
  .s-materials h3{color:var(--red)}
  .dedicated{position:absolute;left:0;top:350px;width:419px;text-align:center;font-size:8px;font-weight:800;color:var(--ink);text-transform:uppercase}
  .thumbs{position:absolute;left:22px;top:368px;display:flex;gap:6px}
  .thumb{width:88px;height:56px;background:linear-gradient(160deg,#8fa2b8,#4b5a6c)}
  .rule{position:absolute;left:0;bottom:0;width:100%;height:8px;background:var(--red)}

  .side-photo{left:0;top:0;width:170px;height:485px;background:linear-gradient(170deg,#9fb3c9 0%,#c8ccd0 45%,#6b7480 100%)}
  .service{position:absolute;left:186px;width:215px}
  .service h3{font-size:8.5px;font-weight:800;color:var(--red);text-transform:uppercase;margin-bottom:4px;display:flex;align-items:center;gap:6px}
  .service p{font-size:6.5px;line-height:1.55;padding-left:24px}
  .icon{width:18px;height:18px;border-radius:50%;background:var(--red);display:inline-flex;align-items:center;justify-content:center;flex:none}
  .svc-1{top:40px}.svc-2{top:170px}.svc-3{top:300px}
</style>
</head>
<body>

<!-- Back cover -->
<section class="page cover-back">
  <svg class="deco" width="429" height="620" viewBox="0 0 429 620" aria-hidden="true">
    <polygon points="300,95 429,95 429,250 330,250" fill="var(--black)"/>
    <polygon points="262,95 300,95 345,250 300,250" fill="var(--red)"/>
    <polygon points="345,250 429,250 429,320" fill="var(--mist)"/>
    <rect x="0" y="600" width="429" height="20" fill="var(--red)"/>
  </svg>
  <div class="brand"><span class="brand-mark"></span>Vexa Trace Heating Ltd</div>

  <ul class="usp-list">
    <li>We design and build complete heat tracing systems</li>
    <li>We install, test and commission all site work</li>
    <li>Full compliance with international standards</li>
    <li>Fast response across the Middle East</li>
    <li>We hold an approved vendor track record</li>
    <li>We own our full supply chain</li>
  </ul>

  <div class="features">
    <p><strong>SMART CONTROL SYSTEMS</strong> specifically tailored to the plant operation ensure safe, efficient heat delivery.</p>
    <p><strong>FULL EPC PACKAGE</strong> from concept and design to installation and long term support.</p>
    <p><strong>DEDICATED PROJECT TEAM</strong> with one point of contact through every phase of the build.</p>
    <p><strong>A COMPLETE SINGLE SOURCE SOLUTION FOR CSP PLANTS</strong></p>
  </div>

  <div class="contact">
    For more details on our capabilities, please contact our sales team:<br>
    <span class="red">Vexa Trace Heating Ltd</span><br>
    Tel: +44 (0) 1632 960 418<br>
    Email: sales@vexatrace.co.uk
  </div>
  <div class="web">www.vexatrace.co.uk</div>
</section>

<!-- Front cover -->
<section class="page cover-front">
  <svg class="deco" width="429" height="620" viewBox="0 0 429 620" aria-hidden="true">
    <polygon points="0,110 200,110 120,460 0,460" fill="#3c3d40"/>
    <polygon points="429,0 429,90 260,90" fill="#4a4b4f"/>
  </svg>
  <svg class="photo front-photo" viewBox="0 0 429 620" role="img" aria-label="Concentrated solar power plant with mirror field and receiver tower">
    <defs>
      <linearGradient id="cspSky" x1="0" y1="0" x2="0" y2="1">
        <stop offset="0" stop-color="#7a8ea6"/>
        <stop offset=".6" stop-color="#c9c3b4"/>
        <stop offset="1" stop-color="#5d6066"/>
      </linearGradient>
    </defs>
    <polygon points="230,110 429,110 429,440 150,440" fill="url(#cspSky)"/>
    <polygon points="205,110 230,110 150,440 125,440" fill="var(--red)"/>
  </svg>

  <div class="logo-box"><div class="brand"><span class="brand-mark"></span>Vexa Trace Heating Ltd</div></div>
  <h1 class="headline">Dedicated Trace Heating Specialists</h1>

  <p class="front-copy">The operation and durability of high temperature heat tracing in CSP concentrated solar power plants is critical to the optimal performance of the plant itself.</p>
  <div class="front-web">www.vexatrace.co.uk</div>
</section>

<!-- Inner left -->
<section class="page inner-left">
  <div class="photo band-photo" role="img" aria-label="Solar thermal collectors against a dusk sky"></div>
  <div class="section s-design">
    <h3>Design</h3>
    <p>Our engineers design every heat tracing circuit around the real operating demands of the solar field. We model heat loss, select cable ratings and plan control zones so each loop holds salt and oil above freezing point with the lowest possible energy use. Drawings, schedules and calculations are delivered ready for client approval.</p>
  </div>
  <div class="section s-materials">
    <h3>Materials</h3>
    <p>We source proven cables, controllers and accessories from approved global manufacturers, matched to the temperature class of each line. All materials are traceable, certified and stored to protect quality until installation on site.</p>
    <p style="margin-top:5px">Careful selection keeps lifetime costs low and gives operators dependable freeze protection across long pipe runs in harsh desert conditions.</p>
  </div>
  <div class="dedicated">Dedicated Trace Heating Specialists</div>
  <div class="thumbs">
    <div class="thumb" role="img" aria-label="Parabolic trough collectors"></div>
    <div class="thumb" role="img" aria-label="Heat traced pipework"></div>
    <div class="thumb" role="img" aria-label="Solar receiver tower"></div>
    <div class="thumb" role="img" aria-label="Mirror field at sunset"></div>
  </div>
  <div class="rule"></div>
</section>

<!-- Inner right -->
<section class="page inner-right">
  <div class="photo side-photo" role="img" aria-label="Rows of solar mirrors in a CSP plant"></div>

  <div class="service svc-1">
    <h3><span class="icon"><svg width="10" height="10" viewBox="0 0 10 10" aria-hidden="true"><path d="M1 5l3 3 5-6" stroke="#fff" stroke-width="1.6" fill="none"/></svg></span>Project Management</h3>
    <p>A dedicated project manager leads each package from award to handover. We plan resources, track progress against programme and report clearly to the main contractor, so the trace heating scope never delays the wider build. Safety and quality checks run at every stage.</p>
  </div>
  <div class="service svc-2">
    <h3><span class="icon"><svg width="10" height="10" viewBox="0 0 10 10" aria-hidden="true"><path d="M1 5l3 3 5-6" stroke="#fff" stroke-width="1.6" fill="none"/></svg></span>Installation Services</h3>
    <p>Our trained site crews install, terminate and test every circuit to specification. We work alongside insulation and mechanical teams, commission control panels and provide full test records, giving owners a system that is ready to run on the first start up.</p>
  </div>
  <div class="service svc-3">
    <h3><span class="icon"><svg width="10" height="10" viewBox="0 0 10 10" aria-hidden="true"><path d="M1 5l3 3 5-6" stroke="#fff" stroke-width="1.6" fill="none"/></svg></span>Cost of Ownership</h3>
    <p>Smart control and correct design cut energy use over the life of the plant. We offer maintenance plans, spares support and remote monitoring so faults are found early and downtime stays low, protecting the value of the investment for decades.</p>
  </div>
  <div class="rule"></div>
</section>

</body>
</html>
```